Business Card Design

New business card design

Target Market(s)

Residential & Commercial Property Managers

Industry/Entity Type

Plumbing Services

Contact Information for Business Card

Name - Owen Tredgold, title - Director, Phone Number - 0431 862 507, email - owen@rvb-plumbing.com.au, Company ABN - 73 215 904 386,

Font styles to use
Sans Serif

Colors
0054AA
0677BA
7BADD7
CADEEF
E8F1F8

```html
<!DOCTYPE html>
<html lang="en">
<head>
<meta charset="utf-8">
<title>RVB Plumbing Services – Business Card</title>
<link href="https://fonts.googleapis.com/css2?family=Montserrat:wght@400;500;700&display=swap" rel="stylesheet">
<style>
  :root {
    --page-bg: #e9ecef;
    --card-dark: #1f262c;
    --card-light: #ffffff;
    --brand-blue: #2aace2;
    --ink: #1c2328;
    --muted: #8a8f93;
    --dark-logo: #3a444c;
  }
  * { margin: 0; padding: 0; box-sizing: border-box; }
  html, body { width: 1200px; height: 912px; overflow: hidden; }
  body {
    background: var(--page-bg);
    font-family: "Montserrat", Arial, sans-serif;
    position: relative;
  }
  .card {
    position: absolute;
    left: 275px;
    width: 650px;
    height: 372px;
    border-radius: 22px;
    overflow: hidden;
    box-shadow: 0 10px 28px rgba(0,0,0,0.18);
  }
  .card--back { top: 40px; background: var(--card-dark); }
  .card--front { top: 492px; background: var(--card-light); }

  .brand-name {
    font-weight: 500;
    color: var(--ink);
    letter-spacing: 0.02em;
  }
  .card--back .brand-name {
    position: absolute;
    left: 0; right: 0; top: 150px;
    text-align: center;
    font-size: 40px;
    color: var(--dark-logo);
  }

  .card--front .brand-name {
    position: absolute;
    left: 58px; top: 52px;
    font-size: 30px;
  }
  .accent-bar {
    position: absolute;
    left: 0; top: 176px;
    width: 18px; height: 58px;
    background: var(--brand-blue);
  }
  .contact {
    position: absolute;
    left: 58px; top: 166px;
  }
  .contact__name {
    font-size: 31px; font-weight: 700; color: var(--brand-blue); line-height: 1.1;
  }
  .contact__title {
    font-size: 21px; color: var(--ink); margin-bottom: 16px;
  }
  .contact__abn { font-size: 18px; color: var(--ink); margin-bottom: 14px; }
  .contact__abn span { color: var(--brand-blue); }
  .contact__line {
    display: flex; align-items: center; gap: 10px;
    font-size: 19px; color: var(--ink); line-height: 1.5;
  }
  .contact__line svg { width: 18px; height: 18px; fill: var(--brand-blue); flex: none; }
  .feature-circle {
    position: absolute;
    right: 60px; top: 96px;
    width: 200px; height: 200px;
    border-radius: 50%;
    background: var(--brand-blue);
  }
</style>
</head>
<body>
  <section class="card card--back" aria-label="Card back">
    <p class="brand-name">RVB Plumbing Services</p>
  </section>

  <section class="card card--front" aria-label="Card front">
    <p class="brand-name">RVB Plumbing Services</p>
    <div class="accent-bar"></div>
    <div class="contact">
      <p class="contact__name">Owen Tredgold</p>
      <p class="contact__title">Director</p>
      <p class="contact__abn"><span>Company ABN</span> - 73 215 904 386</p>
      <p class="contact__line">
        <svg viewBox="0 0 24 24" aria-hidden="true"><path d="M6.6 10.8a15.1 15.1 0 0 0 6.6 6.6l2.2-2.2a1 1 0 0 1 1-.25 11.4 11.4 0 0 0 3.6.57 1 1 0 0 1 1 1V20a1 1 0 0 1-1 1A17 17 0 0 1 3 4a1 1 0 0 1 1-1h3.5a1 1 0 0 1 1 1c0 1.25.2 2.45.57 3.57a1 1 0 0 1-.25 1z"/></svg>
        0431 862 507
      </p>
      <p class="contact__line">
        <svg viewBox="0 0 24 24" aria-hidden="true"><path d="M2 5h20v14H2zm2 2v.4l8 5.1 8-5.1V7zm0 2.8V17h16V9.8l-8 5.1z"/></svg>
        owen@rvb-plumbing.com.au
      </p>
    </div>
    <div class="feature-circle"></div>
  </section>
</body>
</html>
```